Business Card for a Dental Office

The design should communicate integrity, quality and reliability. We also want the card look elegant, simple, but still stand out, different from the traditional-dental-office business card.

Business

```html
<!DOCTYPE html>
<html lang="en">
<head>
<meta charset="utf-8">
<title>Harlow Dental Studio – Business Cards</title>
<link rel="stylesheet" href="https://fonts.googleapis.com/css2?family=Open+Sans:wght@400;600;700&display=swap">
<style>
  :root {
    --stage: #8d8f91;
    --card-white: #ffffff;
    --card-black: #141414;
    --card-black-edge: #1f1f1f;
    --ink: #1a1a1a;
    --gold: #cfae1e;
    --gold-soft: #b8972a;
    --white: #f4f4f4;
    --rule: #3a3a3a;
  }
  * { margin: 0; padding: 0; box-sizing: border-box; }
  html, body { width: 1200px; height: 900px; overflow: hidden; }
  body {
    background: var(--stage);
    font-family: "Open Sans", Arial, sans-serif;
    position: relative;
  }
  .card {
    position: absolute;
    width: 600px;
    height: 340px;
    border-radius: 4px;
    box-shadow: 0 10px 24px rgba(0,0,0,0.25);
    overflow: hidden;
  }

  /* Shared brand lockup */
  .brand { display: flex; align-items: center; gap: 10px; white-space: nowrap; }
  .brand-mark { width: 28px; height: 28px; background: var(--gold); flex: none; }
  .brand-name {
    font-weight: 700;
    font-size: 23px;
    letter-spacing: 0.4px;
    text-transform: uppercase;
    line-height: 1;
  }
  .tagline {
    font-weight: 700;
    font-size: 11px;
    letter-spacing: 1.5px;
    text-transform: uppercase;
    color: var(--gold);
    margin: 5px 0 0 38px;
    white-space: nowrap;
  }

  /* Appointment card */
  .appointment-card {
    left: 480px; top: 70px;
    background: var(--card-white);
    color: var(--ink);
  }
  .appointment-card .brand-block { position: absolute; left: 200px; top: 30px; }
  .appointment-title {
    position: absolute; left: 238px; top: 86px;
    font-size: 19px; font-weight: 600;
    color: var(--gold-soft);
    white-space: nowrap;
  }
  .field {
    position: absolute; left: 60px; width: 500px;
    display: flex; align-items: flex-end;
    font-size: 14px; font-weight: 700;
    white-space: nowrap;
  }
  .field .dots {
    flex: 1;
    border-bottom: 2px dotted var(--ink);
    margin: 0 8px 4px;
  }
  .field-name { top: 128px; }
  .field-date { top: 166px; }
  .field-time { top: 204px; }
  .field-pm { top: 242px; left: 250px; width: 310px; }
  .field-pm .dots { margin-left: 0; }
  .notice {
    position: absolute; left: 60px; top: 284px;
    font-size: 15px; font-weight: 600;
    white-space: nowrap;
  }

  /* Business card */
  .business-card {
    left: 120px; top: 480px;
    background: linear-gradient(135deg, var(--card-black-edge), var(--card-black) 60%);
    color: var(--white);
  }
  .person { position: absolute; left: 36px; top: 58px; }
  .person-name { font-size: 20px; font-weight: 600; color: var(--gold); }
  .person-title { font-size: 14px; margin-top: 2px; }
  .business-card .brand-block { position: absolute; left: 236px; top: 40px; }
  .business-card .brand-name { color: var(--white); }
  .divider {
    position: absolute; left: 240px; right: 36px; top: 152px;
    height: 1px; background: var(--rule);
  }
  .contact {
    position: absolute; right: 32px; bottom: 36px;
    list-style: none; text-align: right;
  }
  .contact li {
    display: flex; align-items: center; justify-content: flex-end; gap: 10px;
    font-size: 16px; line-height: 24px;
  }
  .contact svg { width: 14px; height: 14px; fill: none; stroke: var(--gold); stroke-width: 1.6; }
</style>
</head>
<body>

<section class="card appointment-card">
  <div class="brand-block">
    <div class="brand">
      <span class="brand-mark"></span>
      <span class="brand-name">Harlow Dental Studio</span>
    </div>
    <div class="tagline">Gentle care for lasting smiles</div>
  </div>
  <p class="appointment-title">Your Next Appointment is</p>
  <div class="field field-name">Name :<span class="dots"></span></div>
  <div class="field field-date">Date :<span class="dots"></span></div>
  <div class="field field-time">Time:<span class="dots"></span>AM</div>
  <div class="field field-pm"><span class="dots"></span>PM</div>
  <p class="notice">If unable to keep appointment, kindly give 24hrs notice.</p>
</section>

<section class="card business-card">
  <div class="person">
    <p class="person-name">Marcus Ellery</p>
    <p class="person-title">Managing Director</p>
  </div>
  <div class="brand-block">
    <div class="brand">
      <span class="brand-mark"></span>
      <span class="brand-name">Harlow Dental Studio</span>
    </div>
    <div class="tagline">Gentle care for lasting smiles</div>
  </div>
  <div class="divider"></div>
  <ul class="contact">
    <li>555.014.2288
      <svg viewBox="0 0 14 14"><rect x="3.5" y="1" width="7" height="12" rx="1.2"/><line x1="6" y1="11" x2="8" y2="11"/></svg>
    </li>
    <li>555.014.2288
      <svg viewBox="0 0 14 14"><path d="M1 5 Q7 1 13 5 L11 7 L9 5.5 L5 5.5 L3 7 Z"/><rect x="3" y="8" width="8" height="5" rx="1"/></svg>
    </li>
    <li>hello@harlowdental.com
      <svg viewBox="0 0 14 14"><rect x="1" y="3" width="12" height="8"/><polyline points="1,3 7,8 13,3"/></svg>
    </li>
    <li>www.harlowdental.com
      <svg viewBox="0 0 14 14"><rect x="1" y="6" width="7" height="4" rx="2" transform="rotate(-45 4.5 8)"/><rect x="6" y="4" width="7" height="4" rx="2" transform="rotate(-45 9.5 6)"/></svg>
    </li>
  </ul>
</section>

</body>
</html>
```